Business Card Design Project

Business Card
We are rebranding with a new logo
Industry/Entity Type
Business
Contact Information for Business Card
Dennis Marlow +61 427581962 dennis@qovo.com.au P.O. Box 872 Kelvindale QLD 4309
Requirements
Must have
- Logo

```html
<!DOCTYPE html>
<html lang="en">
<head>
<meta charset="utf-8">
<title>Qovo International – Business Card</title>
<link rel="stylesheet" href="https://fonts.googleapis.com/css2?family=Roboto:wght@400;500&family=Roboto+Condensed:wght@700&display=swap">
<style>
  :root {
    --backdrop: #1e1e1e;
    --card: #f2f2f2;
    --brand-blue: #1b90c9;
    --blue-deep: #0a6fa8;
    --blue-light: #a9dcf2;
    --brand-orange: #f0782a;
    --orange-light: #f5d2b6;
    --text: #4a4a4a;
    --rule: #a9a9a9;
  }
  * { margin: 0; padding: 0; box-sizing: border-box; }
  html, body {
    width: 1200px; height: 960px; overflow: hidden;
    background: var(--backdrop);
  }
  .business-card {
    position: absolute; left: 314px; top: 295px;
    width: 600px; height: 342px;
    background: var(--card);
    border-radius: 16px;
    overflow: hidden;
    font-family: "Roboto", sans-serif;
  }
  .edge-band { position: absolute; top: 0; bottom: 0; width: 9px; }
  .edge-band--left {
    left: 0;
    background: linear-gradient(to bottom, var(--blue-deep), var(--brand-blue) 45%, var(--blue-light));
  }
  .edge-band--right {
    right: 0;
    background: linear-gradient(to bottom, var(--orange-light), #f3a468 50%, var(--brand-orange));
  }
  .brand-name {
    position: absolute; right: 30px; top: 120px;
    font-family: "Roboto", sans-serif; font-weight: 500;
    font-size: 20px; letter-spacing: 2px;
    color: var(--brand-blue);
    text-transform: uppercase;
  }
  .holder-name {
    position: absolute; left: 25px; top: 195px;
    font-family: "Roboto Condensed", sans-serif; font-weight: 700;
    font-size: 21px; color: var(--brand-blue);
    text-transform: uppercase;
  }
  .divider {
    position: absolute; left: 26px; right: 30px; top: 229px;
    height: 1px; background: var(--rule);
  }
  .contact-list {
    position: absolute; left: 26px; top: 239px;
    list-style: none; font-size: 14px; color: var(--text);
  }
  .contact-list li { display: flex; align-items: center; height: 19px; }
  .contact-list svg { width: 14px; height: 14px; margin-right: 8px; fill: var(--brand-blue); }
  .postal-address {
    position: absolute; right: 26px; top: 259px;
    font-style: normal; font-size: 14px; line-height: 19px;
    color: var(--text); text-align: right;
  }
</style>
</head>
<body>
  <article class="business-card">
    <div class="edge-band edge-band--left" role="img" aria-label="Blue decorative edge trim"></div>
    <div class="edge-band edge-band--right" role="img" aria-label="Orange decorative edge trim"></div>

    <div class="brand-name">Qovo International</div>

    <h1 class="holder-name">Dennis Marlow</h1>
    <div class="divider"></div>

    <ul class="contact-list">
      <li>
        <svg viewBox="0 0 24 24" aria-hidden="true"><path d="M6.6 10.8c1.4 2.8 3.8 5.1 6.6 6.6l2.2-2.2c.3-.3.7-.4 1-.2 1.1.4 2.3.6 3.6.6.6 0 1 .4 1 1V20c0 .6-.4 1-1 1C10.6 21 3 13.4 3 4c0-.6.4-1 1-1h3.5c.6 0 1 .4 1 1 0 1.3.2 2.5.6 3.6.1.3 0 .7-.2 1z"/></svg>
        +61 427581962
      </li>
      <li>
        <svg viewBox="0 0 24 24" aria-hidden="true"><path d="M2 5h20v14H2z"/><path d="M3 6.5l9 6.5 9-6.5" fill="none" stroke="#fff" stroke-width="1.5"/></svg>
        dennis@qovo.com.au
      </li>
      <li>
        <svg viewBox="0 0 24 24" aria-hidden="true"><circle cx="12" cy="12" r="10"/><path d="M2 12h20M12 2c3 3 3 17 0 20M12 2c-3 3-3 17 0 20" fill="none" stroke="#fff" stroke-width="1.4"/></svg>
        www.qovo.com.au
      </li>
    </ul>

    <address class="postal-address">
      P.O. Box 872<br>
      Kelvindale QLD 4309
    </address>
  </article>
</body>
</html>
```